Tarvek Mailbox Services, full-service collaboration with postal service - installation of units

1. CBU - Cluster Box Unit - These are Mailbox units that you would see at residential neighborhoods, and Apartments -
2. Logo Needed
3. Maybe have CBU as a division of DWHS (Dorian Whitcombe Home Services)
4. Card to be primary Tarvek Mailbox Services

This is a letter of introduction that I am developing:

I am writing to introduce Dorian Whitcombe Home Services, a company dedicated to delivering exceptional service and quality in the installation and maintenance of commercial mailboxes, specifically Cluster Box Units (CBUs). Our commitment to excellence and customer satisfaction has established us as a trusted partner for developers and postal services alike.
At Dorian Whitcombe Home Services, we take pride in our comprehensive approach, ensuring that every step of the mailbox installation process is handled with precision and care. Our services include:
• Supplying high-quality CBUs tailored to meet the specific needs of your development.
• Providing a CBU plat layout upon approval of the address plat, ensuring seamless integration into your development plans.
• Collaborating with developers and postmasters to determine the optimal CBU locations for efficient mail delivery.
• Qualifying the labeling of CBU units, offering both sticker and etching options to suit your preferences.
• Pouring durable concrete foundations as required for the secure installation of the CBU units.
• Handling the installation process with expertise and attention to detail.
• Labeling the units and supplying keys for each mailbox, ensuring a smooth transition for residents and businesses.
Our team is dedicated to working closely with you to ensure that all requirements are met and that the installation process is completed efficiently and to the highest standards.
We look forward to the opportunity to collaborate with you and contribute to the success of your project. Please do not hesitate to contact us for any additional information or to discuss your specific requirements.
Sincerely,
Dorian Whitcombe
Dorian Whitcombe Home Services

Target Market(s)

Developers, Builders, Apartment's, HOA

Industry/Entity Type

Construction

Contact Information for Business Card

Name: Dorian Whitcombe, Cell:555-017-6481, Email: dori@dwhomeworks.example

Font styles to use
Serif

Requirements
Must have
• Fresh Looking
Nice to have
• Maybe a CBU Box if it looks clean
Should not have
• Not Industrial or Old traditional card

```html
<!DOCTYPE html>
<html lang="en">
<head>
<meta charset="utf-8">
<title>Tarvek Mailbox Services – Business Card</title>
<link href="https://fonts.googleapis.com/css2?family=Poppins:wght@300;600;700&display=swap" rel="stylesheet">
<style>
  :root {
    --blue: #13a0c3;
    --green: #3dab4a;
    --green-dark: #1e8741;
    --grey-panel: #e6e7e8;
    --ink-soft: #8a8a8a;
    --paper: #ffffff;
    --page: #ffffff;
  }
  * { margin: 0; padding: 0; box-sizing: border-box; }
  html, body {
    width: 960px; height: 1200px; overflow: hidden;
    background: var(--page);
    font-family: "Poppins", Arial, sans-serif;
  }
  .canvas { position: relative; width: 960px; height: 1200px; }
  .card {
    position: absolute; left: 60px; width: 840px; height: 480px;
    background: var(--paper); overflow: hidden;
    box-shadow: 0 0 0 1px #f1f1f1;
  }
  .card--front { top: 86px; }
  .card--back { top: 634px; }

  .front-art { position: absolute; left: 0; top: 0; width: 440px; height: 480px; }

  .brand-front {
    position: absolute; left: 52px; top: 196px; width: 250px;
    color: var(--paper); font-weight: 600; text-transform: uppercase;
    text-align: center; line-height: 1.35;
  }
  .brand-front .brand-main { display: block; font-size: 30px; letter-spacing: 10px; padding-left: 10px; }
  .brand-front .brand-sub { display: block; font-size: 13px; letter-spacing: 3px; }

  .contact { position: absolute; left: 484px; top: 160px; width: 336px; }
  .contact__name {
    font-size: 26px; font-weight: 700; letter-spacing: 0.3px;
    text-transform: uppercase; color: var(--blue); white-space: nowrap;
  }
  .contact__name .surname { color: var(--green); }
  .contact__rule { margin-top: 14px; width: 273px; height: 2px; background: var(--blue); }
  .contact__list { list-style: none; margin-top: 22px; }
  .contact__item {
    display: flex; align-items: center; height: 34px;
    font-size: 18px; font-weight: 300; color: var(--ink-soft); white-space: nowrap;
  }
  .contact__icon { width: 34px; height: 34px; flex: none; margin-right: 22px; }
  .contact__icon--phone { background: var(--green); }
  .contact__icon--mail { background: var(--blue); }

  .band { position: absolute; left: 0; width: 100%; height: 86px; }
  .band--top { top: 0; background: var(--blue); }
  .band--bottom { bottom: 0; background: var(--green); }

  .brand-back {
    position: absolute; left: 0; top: 185px; width: 100%;
    text-align: center; color: var(--green); font-weight: 600;
    text-transform: uppercase; line-height: 1.3;
  }
  .brand-back .brand-main { display: block; font-size: 54px; letter-spacing: 24px; padding-left: 24px; }
  .brand-back .brand-sub { display: block; font-size: 24px; letter-spacing: 6px; padding-left: 6px; }
</style>
</head>
<body>
<main class="canvas">

  <section class="card card--front" aria-label="Business card front">
    <svg class="front-art" viewBox="0 0 440 480" aria-hidden="true">
      <rect x="0" y="0" width="367" height="480" fill="var(--grey-panel)"/>
      <polygon points="367,0 184,100 367,200" fill="var(--green)"/>
      <polygon points="184,100 204,89 367,178 367,200" fill="var(--green-dark)"/>
      <polygon points="367,480 184,380 367,280" fill="var(--green)"/>
      <polygon points="184,380 204,391 367,302 367,280" fill="var(--green-dark)"/>
      <polygon points="0,0 440,240 0,480" fill="var(--blue)"/>
    </svg>

    <div class="brand-front">
      <span class="brand-main">Tarvek</span>
      <span class="brand-sub">Mailbox Services</span>
    </div>

    <div class="contact">
      <h1 class="contact__name">Dorian <span class="surname">Whitcombe</span></h1>
      <div class="contact__rule"></div>
      <ul class="contact__list">
        <li class="contact__item">
          <svg class="contact__icon contact__icon--phone" viewBox="0 0 34 34" aria-label="Phone" role="img">
            <path d="M11 8c1-1 2.2-.8 2.8.2l1.9 3.3c.5.9.2 1.9-.6 2.4l-1.3.9c1 2.6 3 4.7 5.5 5.8l1-1.3c.6-.8 1.6-1 2.4-.5l3.2 2c1 .6 1.1 1.900.2 2.8l-1.6 1.6c-1.2 1.200-3 1.500-4.6.8C14.6 24.2 9.8 19.4 8 14.1c-.6-1.600-.2-3.400 1-4.600z" fill="#fff"/>
          </svg>
          555-017-6481
        </li>
        <li class="contact__item">
          <svg class="contact__icon contact__icon--mail" viewBox="0 0 34 34" aria-label="Email" role="img">
            <rect x="7" y="10" width="20" height="14" fill="none" stroke="#fff" stroke-width="1.6"/>
            <polyline points="7,10 17,18 27,10" fill="none" stroke="#fff" stroke-width="1.6"/>
            <polyline points="7,24 14,16" fill="none" stroke="#fff" stroke-width="1.2"/>
            <polyline points="27,24 20,16" fill="none" stroke="#fff" stroke-width="1.2"/>
          </svg>
          dori@dwhomeworks.example
        </li>
      </ul>
    </div>
  </section>

  <section class="card card--back" aria-label="Business card back">
    <div class="band band--top"></div>
    <div class="brand-back">
      <span class="brand-main">Tarvek</span>
      <span class="brand-sub">Mailbox Services</span>
    </div>
    <div class="band band--bottom"></div>
  </section>

</main>
</body>
</html>
```